Mission Statement Board for front lobby

We need a mission statement board for our front lobby at our company called LoomHarbor. We are a web content management company that builds websites for our clients. We would like two boards, same size, canvas material (not thin poster board or anything like that) size H 3' x L 2', white background, blue and black colored font, our logo on top in blue/gray/black and some blue coloring around top and bottom, kind of framing the white background. Please reference our very rough draft we did in Word so you get an idea of what we're thinking- the attachment shows what we would like on each board. Reference our website to see logo and fonts if you would like, please keep the board similar to our fonts and colors. www.loomharbor-example.com

Contact info: Marta Quimby
Email: marta.quimby@loomharbor-example.com
Phone: 555-217-0493
Updates

Please do not include in a design my contact info, no email marta.quimby@loomharbor-example.com, no phone # 555-217-0493. I added that info to the project when I posted it, but it is not part of the design.... reference attachment posted in project with exactly what we want.

Target Market(s)

Clients & employees in the office who will see the boards in lobby

Industry/Entity Type

It Company

Font styles to use
Other font styles liked:
• reference attachment (but font is flexible within reason)

Colors
33a6d7
0255a3
eaf1f7
0292cd
85cae6
cee9f5
000000
5c5c5c
959595

Requirements
Must have
• Needs to be a professional sign that hangs on wall, company logo, cohesive colors and fonts
Nice to have
• Get creative with the border/framing around the white background
Should not have
• Unprofessional fonts, typos, thin cheap looking poster board materal.

```html
<!DOCTYPE html>
<html lang="en">
<head>
<meta charset="utf-8">
<title>LoomHarbor – Mission Statement Board</title>
<link href="https://fonts.googleapis.com/css2?family=Open+Sans:wght@400;600;700&display=swap" rel="stylesheet">
<style>
  :root {
    --sky: #33a6d7;
    --brand-blue: #0292cd;
    --deep-blue: #0255a3;
    --navy: #0a4e9e;
    --mist: #eaf1f7;
    --pale: #cee9f5;
    --ink: #111111;
    --slate: #3c3c3c;
    --stage: #3a3a3a;
    --white: #ffffff;
  }
  * { box-sizing: border-box; margin: 0; padding: 0; }
  html, body { width: 1016px; height: 1200px; overflow: hidden; }
  body {
    background: var(--stage);
    font-family: "Open Sans", Arial, sans-serif;
  }
  .board {
    position: absolute; left: 128px; top: 30px;
    width: 760px; height: 1140px;
    background: linear-gradient(90deg, #f4f9fd 0%, var(--mist) 40%, #d9ebf7 100%);
    overflow: hidden;
  }
  .hero { position: absolute; left: 0; top: 0; width: 760px; height: 511px; }
  .hero svg { position: absolute; left: 0; top: 0; }
  .hero-text { position: absolute; left: 32px; color: var(--white); }
  .hero-heading {
    font-weight: 600; font-size: 29px; line-height: 29px;
    border-bottom: 2px solid var(--white); padding-bottom: 3px;
  }
  .mission { top: 130px; }
  .mission .hero-heading { width: 236px; }
  .hero-body { font-size: 20px; line-height: 29px; margin-top: 8px; }
  .faith { top: 380px; }
  .faith .hero-heading { font-size: 36px; line-height: 40px; width: 236px; padding-bottom: 0; }
  .values-tab {
    position: absolute; left: 0; top: 540px; width: 276px; height: 53px;
    background: var(--navy); color: var(--white);
    border-radius: 0 8px 8px 0;
    font-weight: 600; font-size: 26px; line-height: 53px; padding-left: 30px;
    box-shadow: 6px 8px 14px rgba(0,0,0,0.18);
  }
  .value { position: absolute; width: 300px; }
  .value h3 {
    display: flex; align-items: center; gap: 8px;
    font-weight: 600; font-size: 28px; line-height: 34px; color: var(--ink);
    margin-left: -30px;
  }
  .value h3 svg { flex: none; }
  .value p { font-size: 15.5px; line-height: 22px; color: var(--slate); margin-top: 6px; }
  .v-integrity { left: 226px; top: 0; }
  .col-left { left: 60px; }
  .col-right { left: 450px; }
  .divider {
    position: absolute; left: 379px; top: 714px; height: 410px;
    border-left: 2px dotted #9bb0c4;
  }
  .brand {
    position: absolute; left: 480px; top: 985px; width: 230px;
    display: flex; align-items: center; gap: 10px;
  }
  .brand-dot { width: 30px; height: 30px; border-radius: 50%; background: var(--brand-blue); }
  .brand-name { font-weight: 700; font-size: 32px; color: var(--deep-blue); }
  .footer { position: absolute; left: 0; top: 1063px; width: 760px; height: 77px; }
  .footer svg { position: absolute; left: 0; top: 0; }
  .footer-url {
    position: absolute; left: 55px; top: 19px;
    color: var(--white); font-size: 28px; line-height: 40px;
  }
  .footer-url b { font-weight: 700; }
</style>
</head>
<body>
<main class="board">
  <section class="hero">
    <svg width="760" height="511" viewBox="0 0 760 511">
      <defs>
        <linearGradient id="heroPhoto" x1="0" y1="0" x2="1" y2="1">
          <stop offset="0" stop-color="#e0a464"/>
          <stop offset="0.45" stop-color="#cdb9a4"/>
          <stop offset="1" stop-color="#8fa1ad"/>
        </linearGradient>
        <linearGradient id="heroBlue" x1="0" y1="0" x2="1" y2="0">
          <stop offset="0" stop-color="#1d8ed0"/>
          <stop offset="1" stop-color="var(--sky)"/>
        </linearGradient>
      </defs>
      <rect x="0" y="0" width="760" height="472" fill="url(#heroBlue)"/>
      <polygon points="232,0 760,0 760,472 430,472" fill="url(#heroPhoto)" role="img" aria-label="Photo of a team working at a laptop and tablet with charts on a desk"/>
      <rect x="0" y="472" width="760" height="28" fill="var(--brand-blue)"/>
      <polygon points="0,472 470,472 486,511 0,511" fill="#3b3b3d"/>
    </svg>
    <div class="hero-text mission" style="top:62px">
      <h2 class="hero-heading">Our Mission Statement</h2>
      <p class="hero-body">We Design And<br>Implement Extraordinary<br>Web Solutions To Help<br>Our Clients Achieve Their<br>Goals.</p>
    </div>
    <div class="hero-text faith" style="top:300px">
      <h2 class="hero-heading">Our Faith...</h2>
      <p class="hero-body">We reflect the love of Christ in us<br>and through us to our fellow<br>employees, partners and clients.</p>
    </div>
  </section>

  <h2 class="values-tab">OUR CORE VALUES</h2>

  <article class="value col-left" style="top:612px">
    <h3><svg width="22" height="22" viewBox="0 0 22 22"><g stroke="var(--deep-blue)" stroke-width="2.4" stroke-linecap="round"><line x1="11" y1="2" x2="11" y2="20"/><line x1="3" y1="6.5" x2="19" y2="15.5"/><line x1="3" y1="15.5" x2="19" y2="6.5"/></g></svg>Integrity</h3>
    <p>We believe that to be successful, it is essential to operate at the highest levels of honesty, responsibility and trust.</p>
  </article>
  <article class="value col-left" style="top:760px">
    <h3><svg width="22" height="22" viewBox="0 0 22 22"><rect x="3" y="2" width="16" height="18" rx="2" fill="var(--deep-blue)"/><g stroke="var(--white)" stroke-width="1.8"><line x1="7" y1="8" x2="15" y2="8"/><line x1="7" y1="12" x2="15" y2="12"/><line x1="7" y1="16" x2="12" y2="16"/></g></svg>Excellence</h3>
    <p>We continually improve our standards and processes so that excellence simple becomes a natural consequence of our work.</p>
  </article>
  <article class="value col-left" style="top:910px">
    <h3><svg width="26" height="22" viewBox="0 0 26 22"><circle cx="17" cy="7" r="5" fill="none" stroke="var(--deep-blue)" stroke-width="2"/><path d="M1 14h6l4 3h8l5-3v4l-6 3H1z" fill="var(--deep-blue)"/></svg>Loyalty</h3>
    <p>Working collaboratively with LoomHarbor employees, partners and customers to solve problems and achieve goals.</p>
  </article>

  <div class="divider"></div>

  <article class="value col-right" style="top:612px">
    <h3><svg width="22" height="22" viewBox="0 0 22 22"><path d="M11 1l9 3v7c0 5-4 8.5-9 10C6 19.5 2 16 2 11V4z" fill="var(--deep-blue)"/><circle cx="11" cy="10" r="3.5" fill="var(--white)"/></svg>Accountability</h3>
    <p>Taking responsibility for one's<br>own actions.</p>
  </article>
  <article class="value col-right" style="top:757px">
    <h3><svg width="22" height="22" viewBox="0 0 22 22"><circle cx="11" cy="11" r="10" fill="var(--deep-blue)"/><circle cx="8" cy="9" r="2.6" fill="var(--white)"/><circle cx="14" cy="9" r="2.6" fill="var(--white)"/><path d="M4 17c1-3 7-3 7 0M11 17c1-3 7-3 7 0" fill="var(--white)"/></svg>Respect</h3>
    <p>Understand and value differences in others. Listen thoughtfully to understand.</p>
  </article>

  <div class="brand">
    <span class="brand-dot"></span>
    <span class="brand-name">LoomHarbor</span>
  </div>

  <footer class="footer">
    <svg width="760" height="77" viewBox="0 0 760 77">
      <polygon points="440,8 760,8 760,77 470,77" fill="var(--deep-blue)"/>
      <polygon points="440,8 452,8 484,77 472,77" fill="var(--sky)"/>
      <polygon points="0,0 440,0 472,77 0,77" fill="var(--navy)"/>
    </svg>
    <p class="footer-url">www.<b>loomharbor-example</b>.com</p>
  </footer>
</main>
</body>
</html>
```